Redesign Login page

I want to redesign my login page to bring my 2 products closer together. I am only looking to redesign one login page, not 2.

For the logo, please make it solid and it can be black or white if helpful. I can also fine tune the logo if you get it close.

Coding

Coded - Design and coding required

Number of Pages Required

1 page

```html
<!DOCTYPE html>
<html lang="en">
<head>
<meta charset="utf-8">
<title>Kelvane – Login</title>
<link rel="stylesheet" href="https://fonts.googleapis.com/css2?family=Poppins:wght@400;500;600;700&display=swap">
<style>
  :root {
    --bg-top: #1d2d2a;
    --bg-bottom: #0b1c19;
    --texture: #2c3e3a;
    --card-a-top: #04302b;
    --card-a-bottom: #476a64;
    --card-b-top: #345a54;
    --card-b-bottom: #1f4540;
    --white: #ffffff;
    --field-text: #6f7674;
    --dark-text: #1c1c1c;
    --button-fill: #4b716a;
    --muted-white: rgba(255,255,255,0.85);
  }
  * { box-sizing: border-box; margin: 0; padding: 0; }
  html, body { width: 1200px; height: 675px; overflow: hidden; }
  body {
    position: relative;
    font-family: "Poppins", sans-serif;
    background: radial-gradient(ellipse at 20% 20%, var(--bg-top), var(--bg-bottom) 80%);
    color: var(--white);
  }
  .line-texture {
    position: absolute; inset: 0;
    background:
      radial-gradient(ellipse 420px 260px at 110px 430px, rgba(80,110,104,0.22), transparent 70%),
      radial-gradient(ellipse 300px 200px at 1060px 90px, rgba(80,110,104,0.2), transparent 70%),
      radial-gradient(ellipse 380px 220px at 300px 600px, rgba(60,90,84,0.15), transparent 70%);
  }
  .login-card { position: absolute; border-radius: 15px; overflow: hidden; }
  .login-card--wide {
    left: 244px; top: 79px; width: 411px; height: 480px;
    background: linear-gradient(180deg, var(--card-a-top) 0%, #1f4641 50%, var(--card-a-bottom) 100%);
  }
  .login-card--narrow {
    left: 701px; top: 61px; width: 251px; height: 527px;
    background: linear-gradient(180deg, var(--card-b-top) 0%, #2a504a 55%, var(--card-b-bottom) 100%);
  }
  .abs { position: absolute; }
  .brand-name {
    position: absolute; left: 0; right: 0; text-align: center;
    font-weight: 700; color: var(--white); letter-spacing: -0.5px;
  }
  .headline { position: absolute; left: 0; right: 0; text-align: center; font-weight: 700; line-height: 1; }
  .subline { position: absolute; left: 0; right: 0; text-align: center; font-weight: 400; line-height: 1; }
  .field {
    position: absolute; background: var(--white); border-radius: 999px;
    display: flex; align-items: center; justify-content: space-between;
    color: var(--field-text);
  }
  .field svg { stroke: #777; fill: none; stroke-width: 1.3; }
  .options-row {
    position: absolute; display: flex; justify-content: space-between; align-items: center;
    color: var(--muted-white);
  }
  .remember { display: flex; align-items: center; gap: 4px; }
  .checkbox { width: 8px; height: 8px; border: 1px solid var(--white); border-radius: 1px; }
  .primary-button {
    position: absolute; background: var(--button-fill); border: 1px solid var(--white);
    border-radius: 999px; display: flex; align-items: center; justify-content: center;
    font-weight: 600; box-shadow: 0 2px 6px rgba(0,0,0,0.25);
  }
  .divider-label { position: absolute; display: flex; align-items: center; justify-content: center; }
  .divider-line { position: absolute; height: 1px; background: var(--muted-white); }
  .social-button {
    position: absolute; background: var(--white); border-radius: 999px;
    display: flex; align-items: center; justify-content: center; gap: 6px;
    color: var(--dark-text); font-size: 7.5px;
  }
  .social-button b { font-weight: 600; }
  .social-dot { width: 13px; height: 13px; border-radius: 50%; }
  .social-dot--orbit { background: #5a7d76; }
  .social-dot--circle { background: #2b5c8a; }
  .signup-line { position: absolute; left: 0; right: 0; text-align: center; }
  .signup-line u { text-underline-offset: 2px; }
</style>
</head>
<body>
  <div class="line-texture" role="img" aria-label="Soft flowing line texture across the background"></div>

  <!-- Wide card -->
  <section class="login-card login-card--wide">
    <div class="brand-name" style="top:30px;font-size:30px;">Kelvane</div>
    <h1 class="headline" style="top:98px;font-size:19px;">LOGIN YOUR ACCOUNT</h1>
    <p class="subline" style="top:124px;font-size:10px;">How to i get started lorem ipsum dolor at?</p>

    <div class="field" style="left:68px;top:152px;width:275px;height:31px;padding:0 14px 0 16px;font-size:7.5px;">
      <span>Enter your email</span>
      <svg width="11" height="11" viewBox="0 0 12 12"><circle cx="6" cy="4" r="2.6"/><path d="M1.2 11.5c0-2.8 2.2-4.4 4.8-4.4s4.8 1.6 4.8 4.4"/></svg>
    </div>
    <div class="field" style="left:68px;top:195px;width:275px;height:31px;padding:0 14px 0 16px;font-size:7.5px;">
      <span>Enter your password</span>
      <svg width="11" height="11" viewBox="0 0 12 12"><path d="M1 6c1.4-2.2 3-3.2 5-3.2s3.6 1 5 3.2c-1.4 2.2-3 3.2-5 3.2S2.4 8.2 1 6z"/><circle cx="6" cy="6" r="1.6"/><path d="M1.5 10.5l9-9"/></svg>
    </div>

    <div class="options-row" style="left:68px;top:237px;width:275px;font-size:7.5px;">
      <span class="remember"><span class="checkbox"></span>Remember Me</span>
      <span>Forget Password*</span>
    </div>

    <div class="primary-button" style="left:68px;top:264px;width:275px;height:33px;font-size:10px;">Login Now</div>

    <div class="divider-line" style="left:92px;top:316px;width:68px;"></div>
    <div class="divider-line" style="left:251px;top:316px;width:68px;"></div>
    <div class="divider-label" style="left:0;right:0;top:309px;font-size:9.5px;font-weight:600;">Or Login with</div>

    <div class="social-button" style="left:68px;top:338px;width:275px;height:32px;">
      <span class="social-dot social-dot--orbit"></span><span>Login with <b>Orbitly</b></span>
    </div>
    <div class="social-button" style="left:68px;top:380px;width:275px;height:32px;">
      <span class="social-dot social-dot--circle"></span><span>Login with <b>Circlenet</b></span>
    </div>

    <div class="divider-line" style="left:93px;top:433px;width:45px;"></div>
    <div class="divider-line" style="left:280px;top:433px;width:40px;"></div>
    <p class="signup-line" style="top:428px;font-size:7.5px;">Don't have any account? <u>Sign Up</u></p>
  </section>

  <!-- Narrow card -->
  <section class="login-card login-card--narrow">
    <div class="brand-name" style="top:36px;font-size:30px;">Kelvane</div>
    <h1 class="headline" style="top:104px;font-size:14px;">LOGIN TO YOUR ACCOUNT</h1>
    <p class="subline" style="top:125px;font-size:8.5px;">How to i get started lorem ipsum dolor at?</p>

    <div class="field" style="left:21px;top:151px;width:210px;height:31px;padding:0 12px 0 11px;font-size:9px;">
      <span>Enter Your User Name</span>
      <svg width="10" height="10" viewBox="0 0 12 12"><circle cx="6" cy="4" r="2.6"/><path d="M1.2 11.5c0-2.8 2.2-4.4 4.8-4.4s4.8 1.6 4.8 4.4"/></svg>
    </div>
    <div class="field" style="left:21px;top:188px;width:210px;height:32px;padding:0 12px 0 11px;font-size:9px;">
      <span>Enter Your Password</span>
      <svg width="10" height="10" viewBox="0 0 12 12"><path d="M1 6c1.4-2.2 3-3.2 5-3.2s3.6 1 5 3.2c-1.4 2.2-3 3.2-5 3.2S2.4 8.2 1 6z"/><circle cx="6" cy="6" r="1.6"/><path d="M1.5 10.5l9-9"/></svg>
    </div>

    <div class="options-row" style="left:21px;top:230px;width:210px;font-size:7.5px;">
      <span class="remember"><span class="checkbox"></span>Remember Me</span>
      <span>Forget Password?</span>
    </div>

    <div class="primary-button" style="left:21px;top:259px;width:210px;height:36px;font-size:10px;font-weight:500;">LOGIN NOW</div>

    <div class="divider-line" style="left:22px;top:390px;width:62px;"></div>
    <div class="divider-line" style="left:168px;top:390px;width:62px;"></div>
    <div class="divider-label" style="left:0;right:0;top:383px;font-size:8.5px;font-weight:500;">Or Login with</div>

    <div class="social-button" style="left:21px;top:410px;width:210px;height:31px;">
      <span class="social-dot social-dot--orbit"></span><span>Login with <b>Orbitly</b></span>
    </div>
    <div class="social-button" style="left:21px;top:448px;width:210px;height:31px;">
      <span class="social-dot social-dot--circle"></span><span>Login with <b>Circlenet</b></span>
    </div>

    <p class="signup-line" style="top:494px;font-size:9.5px;">Don't have an account? <u>Sign Up</u></p>
  </section>
</body>
</html>
```